Letterhead and Envelopes design using existing logo. Logo can be found at tlventures.net

Use existing logo (attached) and incorporate in letterhead and envelope designs.

Current logo can be viewed at tlventures.net the web site reflect various parent and sub companies. Please see attached as well.

Target Market(s)

Other oil and gas operators.

Industry/Entity Type

Oil And Gas

Font styles to use
Sans Serif

Colors

Designer to choose colors to be used in the design.

Requirements
Must have
• Current logo and address
Nice to have
• Modern, contemporary approach yet incorporate existing traditional design.
• After design is selected for Ridgemont Caldera Holdings I will use similar design for Royalties, Exploration, Energy and Farms with different color schemes.

```html
<!DOCTYPE html>
<html lang="en">
<head>
<meta charset="UTF-8">
<title>Ridgemont Caldera Holdings — Letterhead</title>
<link href="https://fonts.googleapis.com/css2?family=Arimo:wght@400;700&family=Roboto+Condensed:wght@400&display=swap" rel="stylesheet">
<style>
  :root {
    --backdrop: #e9eaeb;
    --paper: #ffffff;
    --brand-green: #8dc63f;
    --ink: #231f20;
    --rule: #8c8c8c;
    --footer-text: #ffffff;
  }
  * { box-sizing: border-box; margin: 0; padding: 0; }
  html, body {
    width: 1200px; height: 1200px; overflow: hidden;
    background: var(--backdrop);
  }
  .letterhead {
    position: absolute; left: 197px; top: 30px;
    width: 806px; height: 1140px;
    background: var(--paper);
    font-family: "Arimo", Arial, sans-serif;
    color: var(--ink);
  }
  .corner-swoosh { position: absolute; left: 0; top: 0; width: 130px; height: 101px; }
  .brand { position: absolute; left: 57px; top: 100px; display: flex; align-items: center; gap: 12px; }
  .brand-mark {
    width: 83px; height: 83px; border-radius: 50%;
    background: var(--brand-green); flex: none;
  }
  .brand-name {
    font-weight: 700; font-size: 16px; line-height: 19.5px;
    text-transform: uppercase; letter-spacing: 0.3px;
  }
  .header-contact {
    position: absolute; left: 480px; top: 101px;
    font-size: 14px; line-height: 22.4px;
  }
  .header-rule {
    position: absolute; left: 44px; top: 228px; width: 717px;
    border-top: 1px solid var(--rule);
  }
  .footer-band {
    position: absolute; left: 0; bottom: 0; width: 100%; height: 77px;
    background: var(--brand-green);
    color: var(--footer-text);
    font-family: "Roboto Condensed", "Arial Narrow", sans-serif;
    font-size: 15px; line-height: 19px; text-align: center;
    padding-top: 16px;
  }
</style>
</head>
<body>
  <main class="letterhead">
    <svg class="corner-swoosh" viewBox="0 0 130 101" aria-hidden="true">
      <path d="M0,0 H130 C118,35 95,55 65,58 C30,60 8,80 0,101 Z" fill="var(--ink)"/>
      <path d="M0,0 H108 C96,30 80,44 56,47 C25,50 6,64 0,86 Z" fill="var(--brand-green)"/>
    </svg>

    <header>
      <div class="brand">
        <span class="brand-mark" aria-hidden="true"></span>
        <div class="brand-name">Ridgemont Caldera<br>Holdings</div>
      </div>
      <address class="header-contact" style="font-style:normal">
        LLC. PO Box 418 Harlow<br>
        Montana - 59036<br>
        Ph: (406) 555.0142<br>
        E-mail: reception@tlventures.net
      </address>
      <div class="header-rule"></div>
    </header>

    <footer class="footer-band">
      LLC. PO Box 418 Harlow, Montana - 59036<br>
      (406)&nbsp; 555 0142 &nbsp;•&nbsp; reception@tlventures.net
    </footer>
  </main>
</body>
</html>
```